Design a few pages of a luxury magazine for the Prestige Aubergerie Lyon

We need a luxury design for our magazine. See the inDesign pages of the current version attached (zip).

Please work primarily on the first double page (Inventez le luxe de demain) that contains only one photo with legend, a title and the text both in French and English. It must be made clear that the text is the same in two different languages (it is not clear enough here).

You can also work on the other two double pages selected. Feedback will be provided and the 10 best pages will be submitted to a vote at the end of the project timespan.

The most important is a classy and luxury design, this will be printed on expensive paper.

See the full brochure here: https://www.prestigeaubergerie.com/brochure/#page=4

Target Market(s)

Students and parents

Industry/Entity Type

Education

Colors

Designer to choose colors to be used in the design.

Requirements
Must have
• Luxury magazine layout, see:
• https://www.findwerk.com/search?q=luxury+magazine+layout&client=safari&rls=en&source=lnms&tbm=isch&sa=X&ved=0ahUKEwitoIDmit7fAhUVShUIHXC2Cd4Q_AUIDigB&biw=1010&bih=702
Nice to have
• The color of the cover that should be used for blue and grey is #393d49.
• Our font for serif titles (from the logo) is Adobe TRAJAN.
Should not have
• flashy colors

```html
<!DOCTYPE html>
<html lang="fr">
<head>
<meta charset="utf-8">
<title>Prestige Aubergerie Lyon — Vivez l'expérience du luxe</title>
<link rel="stylesheet" href="https://fonts.googleapis.com/css2?family=Fira+Sans:wght@300;400;600;700&family=Libre+Caslon+Text:wght@400;700&display=swap">
<style>
  :root {
    --paper: #ffffff;
    --ink: #2b2b2b;
    --ink-soft: #3c3c3c;
    --gold: #b8a77c;
    --white: #ffffff;
  }
  * { margin: 0; padding: 0; box-sizing: border-box; }
  html, body { width: 1200px; height: 764px; overflow: hidden; background: var(--paper); }
  .spread { position: relative; width: 1200px; height: 764px; font-family: "Fira Sans", sans-serif; color: var(--ink); }

  /* Left page */
  .page-left { position: absolute; left: 0; top: 0; width: 602px; height: 764px; overflow: hidden; }
  .photo-lobby {
    position: absolute; inset: 0;
    background:
      radial-gradient(ellipse 40% 22% at 50% 12%, #8fb4cf 0%, #4d7391 45%, transparent 80%),
      radial-gradient(ellipse 30% 25% at 50% 58%, #8a4a35 0%, transparent 80%),
      linear-gradient(180deg, #2c3a44 0%, #3b3a33 35%, #4a3d30 60%, #1f1b18 100%);
  }
  .feature-note { position: absolute; left: 35px; top: 33px; width: 160px; color: var(--white); }
  .feature-note .note-title { font-family: "Libre Caslon Text", serif; font-size: 9.5px; line-height: 12px; }
  .feature-note .note-title-en { font-family: "Libre Caslon Text", serif; font-size: 9.5px; font-weight: 700; line-height: 12px; margin-bottom: 8px; }
  .feature-note p { font-size: 8.6px; line-height: 10.6px; font-weight: 300; }
  .feature-note p.en { font-weight: 600; margin-top: 9px; }
  .page-title {
    position: absolute; left: 68px; top: 486px; color: var(--white);
    font-size: 64px; font-weight: 600; line-height: 74px; letter-spacing: -0.5px;
  }

  /* Right page */
  .page-right { position: absolute; left: 639px; top: 0; width: 532px; height: 764px; }
  .photo-students {
    position: absolute; left: 0; top: 0; width: 532px; height: 295px;
    background:
      radial-gradient(ellipse 22% 35% at 18% 20%, #2f8f86 0%, transparent 90%),
      radial-gradient(ellipse 25% 40% at 60% 18%, #c9362c 0%, transparent 90%),
      linear-gradient(180deg, #5b4c44 0%, #2a2523 60%, #141212 100%);
  }
  .photo-caption {
    position: absolute; left: 404px; top: 193px; width: 128px; height: 102px;
    background: var(--paper); padding: 4px 0 0 6px;
    font-size: 6.2px; line-height: 8px; font-weight: 300; color: var(--ink);
  }
  .photo-caption .en { margin-top: 3px; }

  .heading-fr { position: absolute; left: 0; top: 320px; font-size: 23px; font-weight: 300; line-height: 28px; color: var(--ink); }
  .heading-en { position: absolute; left: 278px; top: 316px; font-size: 23px; font-weight: 300; line-height: 28.5px; color: var(--gold); }
  .body-fr, .body-en {
    position: absolute; font-size: 9.6px; line-height: 14.6px; font-weight: 300;
    color: var(--ink-soft); text-align: justify;
  }
  .body-fr { left: 0; top: 391px; width: 266px; }
  .body-en { left: 278px; top: 424px; width: 254px; font-size: 9.4px; line-height: 14.4px; letter-spacing: -0.05px; }

  .photo-ceremony {
    position: absolute; left: 0; top: 581px; width: 256px; height: 183px;
    background:
      radial-gradient(ellipse 30% 40% at 30% 60%, #7a3a3a 0%, transparent 85%),
      radial-gradient(ellipse 25% 50% at 72% 70%, #26304a 0%, transparent 85%),
      linear-gradient(180deg, #3a2424 0%, #1c1a1c 100%);
  }
  .hotel-mark { position: absolute; left: 346px; top: 606px; width: 118px; text-align: center; color: var(--ink); }
  .hotel-mark .mark-square { display: block; width: 14px; height: 14px; background: var(--gold); margin: 0 auto 6px; }
  .hotel-mark .mark-name { font-size: 13px; font-weight: 400; line-height: 16px; }
  .hotel-mark .mark-rule { display: block; width: 92px; height: 1px; background: var(--ink); margin: 3px auto 2px; }
  .hotel-mark .mark-city { font-size: 6px; letter-spacing: 1.5px; }
  .ceremony-caption { position: absolute; left: 278px; top: 668px; width: 254px; font-size: 6.2px; line-height: 8px; font-weight: 300; color: var(--ink); }
  .ceremony-caption .en { margin-top: 4px; }
</style>
</head>
<body>
<main class="spread">
  <section class="page-left">
    <div class="photo-lobby" role="img" aria-label="Lobby of a Paris palace hotel with a glass dome, crystal chandelier and grand staircase"></div>
    <div class="feature-note">
      <div class="note-title">Une nuit au Palace</div>
      <div class="note-title-en">A night at the Palace</div>
      <p>Vivez une expérience unique, ici au Maison Lumière Paris. L'opportunité de rencontrer, en tant que client, l'ensemble du personnel dans l'hôtellerie de luxe afin de mieux comprendre et appréhender l'exigence requise dans les établissements haut-de-gamme</p>
      <p class="en">Enjoy a unique experience, here at the Maison Lumière Paris. The opportunity to experience a luxury hotel as a guest, so that you can gain a better understanding of the challenges in luxury establishments</p>
    </div>
    <h1 class="page-title">Vivez<br>l'expérience<br>du luxe…</h1>
  </section>

  <section class="page-right">
    <div class="photo-students" role="img" aria-label="Bachelor students in dark suits posing in the lounge of a palace hotel"></div>
    <div class="photo-caption">
      <p>Les étudiants en Bachelor dans les salons du Palace Le Belvédère Paris à l'occasion d'une formation sur l'apparence pour se familiariser avec les codes du luxe, en immersion dans les plus beaux hôtels</p>
      <p class="en">Students in our Bachelor's degree attending a seminar on personal grooming at the Belvédère, giving them an opportunity to familiarise themselves with luxury codes and gain immersive experience in one of the newest Palace in Paris</p>
    </div>

    <h2 class="heading-fr" lang="fr">…et devenez- en le<br>meilleur Ambassadeur</h2>
    <h2 class="heading-en" lang="en">Experience the luxury<br>sector and become<br>its finest ambassador</h2>

    <p class="body-fr" lang="fr">Au sein de la Prestige Aubergerie Lyon, vous suivez un programme consacré au luxe pour vous imprégner au mieux de cet univers hors du commun et pouvoir en appréhender tous les aspects. La posture, le protocole, la gestuelle, l'apparence : c'est en suivant des cours en immersion et en vivant des expériences concrètes dans les plus beaux hôtels que vous en mesurerez toute l'importance. Avec “Une nuit au Palace”, “Luxury Shopping”, “Goutez le Luxe”, “Afternoon tea” et tant d'autres activités, vous découvrez, du point de vue d'un client, le luxe et l'art de vivre et de recevoir à la française. Ce programme unique vous transmet les codes, les savoir-faire et les savoir-être de l'hôtellerie de luxe.</p>
    <p class="body-en" lang="en">Studying at the Prestige Aubergerie Lyon, you will follow a programme that is 100% focused on luxury so that you can really soak up this extraordinary world and get an understanding of every aspect. By following our immersive classes and gaining concrete experience in the most incredible hotels, you'll learn just how important luxury attitude is. With our programmes “A night at the Palace”, “Luxury Shopping”, “A Taste of Luxury”, “Afternoon tea” and a whole host of other activities, you will get a taste of what life is like for luxury guests and experience the luxury sector and the French art of living. This unique programme will provide you with a first-hand understanding and experience of the luxury hotel industry.</p>

    <div class="photo-ceremony" role="img" aria-label="Graduate holding her diploma beside the hotel director at the award ceremony"></div>

    <div class="hotel-mark">
      <span class="mark-square"></span>
      <div class="mark-name">Maison Lumière</div>
      <span class="mark-rule"></span>
      <div class="mark-city">PARIS</div>
    </div>
    <div class="ceremony-caption">
      <p lang="fr">Le Maison Lumière Paris, somptueux cadre de la remise des diplômes de la Prestige Aubergerie Lyon en 2013, en présence du parrain Julien Marceau (à droite), Directeur du Palace parisien : “Vous pouvez être très fiers de votre formation et de votre diplôme qui vous donnent des atouts importants pour votre future carrière.”</p>
      <p class="en" lang="en">The Maison Lumière Paris, a sumptuous setting for awarding the PA degrees in 2013, with the presence of our sponsor Julien Marceau (right), director of this luxury Parisian hotel: “You can be very proud of your training and diploma as they provide you with important skills for your future career.”</p>
    </div>
  </section>
</main>
</body>
</html>
```